IT Consulting Business Card Design

We need a business card on our company name....which is a IT consulting and staffing company. We also train masters graduates in various IT courses. 70% of the time these cards will be handed out to the graduate students at the universities. 30% for our clients and business partners. We are uploading our company logo...would like to see something that matches our logo or blends with it. Please visit www.brightvaleworks.com for more details on logo and colors.

Target Market(s)

70% of the time these cards will be handed out to the graduate students at the universities. 30% for our clients and business partners.

Industry/Entity Type

Business

Contact Information for Business Card

Ravi Kondamuri
Vice-President
Bright Vale Works Inc
3807 Morrow Lane, Suite 412
East Brookridge, NJ 07315
ravi@brightvaleworks.com
Office : 1-866-219-3840 X 515
Cell number : 732-581-9034

Requirements
Nice to have
• may be company logo and name on the back of the card and detials on the other side...just a thought..!!

```html
<!DOCTYPE html>
<html lang="en">
<head>
<meta charset="utf-8">
<title>Bright Vale Works – Business Card</title>
<link rel="stylesheet" href="https://fonts.googleapis.com/css2?family=Lato:wght@400;700&family=Oswald:wght@600&display=swap">
<style>
  :root {
    --ink: #111111;
    --red: #e01f26;
    --paper: #ffffff;
    --grey-text: #5a5a5a;
    --light-text: #d6d6d6;
    --backdrop: #e9e7e4;
  }
  html, body {
    margin: 0;
    width: 1200px;
    height: 832px;
    overflow: hidden;
    background: var(--backdrop);
  }
  .canvas {
    position: relative;
    width: 1200px;
    height: 832px;
  }
  .card {
    position: absolute;
    top: 262px;
    width: 540px;
    height: 308px;
    background: var(--paper);
    overflow: hidden;
    box-shadow: 0 6px 18px rgba(0,0,0,0.18);
  }
  .card-front { left: 50px; }
  .card-back { left: 610px; }
  .card-art {
    position: absolute;
    inset: 0;
  }
  .person {
    position: absolute;
    right: 22px;
    top: 18px;
    text-align: right;
    font-family: 'Lato', sans-serif;
  }
  .person-name {
    color: var(--red);
    font-size: 19px;
    font-weight: 400;
    margin: 0;
  }
  .person-title {
    color: var(--light-text);
    font-size: 10.5px;
    font-weight: 700;
    letter-spacing: 1.2px;
    margin: 2px 0 0;
  }
  .contact {
    position: absolute;
    right: 22px;
    top: 158px;
    text-align: right;
    font-family: 'Lato', sans-serif;
    font-size: 11px;
    line-height: 14px;
    color: var(--grey-text);
    letter-spacing: 0.3px;
    margin: 0;
  }
  .contact dt { display: inline; font-weight: 700; }
  .contact dd { display: inline; margin: 0; }
  .contact div { margin: 0; }
  .company-name {
    font-family: 'Oswald', sans-serif;
    font-weight: 600;
    color: var(--ink);
    margin: 0;
    letter-spacing: 0.3px;
  }
  .card-front .company-name {
    position: absolute;
    right: 22px;
    top: 222px;
    font-size: 28px;
    line-height: 1;
  }
  .brand-lockup {
    position: absolute;
    left: 0;
    right: 0;
    top: 118px;
    display: flex;
    align-items: center;
    justify-content: center;
    gap: 12px;
  }
  .brand-dot {
    width: 26px;
    height: 26px;
    border-radius: 50%;
    background: var(--red);
  }
  .card-back .company-name {
    font-size: 26px;
    line-height: 1;
  }
  .address-band {
    position: absolute;
    left: 0;
    right: 0;
    bottom: 0;
    height: 56px;
    background: var(--ink);
    display: flex;
    align-items: center;
    justify-content: center;
    font-family: 'Lato', sans-serif;
    font-size: 11.5px;
    letter-spacing: 1.4px;
    color: #9a9a9a;
    margin: 0;
  }
</style>
</head>
<body>
<main class="canvas">
  <section class="card card-front" aria-label="Card front">
    <svg class="card-art" viewBox="0 0 540 308" width="540" height="308" aria-hidden="true">
      <path d="M0 0 H540 V66 C420 92 260 150 150 196 C100 218 50 240 0 252 Z" fill="var(--ink)"/>
      <path d="M0 252 C50 240 100 218 150 196 C260 150 420 92 540 66" fill="none" stroke="var(--red)" stroke-width="9"/>
      <path d="M0 308 V296 C180 290 380 270 540 252 V308 Z" fill="var(--ink)"/>
      <path d="M0 296 C180 290 380 270 540 252" fill="none" stroke="var(--red)" stroke-width="4"/>
    </svg>
    <header class="person">
      <p class="person-name">Mr. Ravi Kondamuri</p>
      <p class="person-title">VICE-PRESIDENT</p>
    </header>
    <dl class="contact">
      <div><dt>cell:</dt> <dd>732-581-9034</dd></div>
      <div><dt>office:</dt> <dd>1-866-219-3840 X 515</dd></div>
      <div><dt>email:</dt> <dd>ravi@brightvaleworks.com</dd></div>
    </dl>
    <p class="company-name">BRIGHT VALE WORKS</p>
  </section>

  <section class="card card-back" aria-label="Card back">
    <div class="brand-lockup">
      <span class="brand-dot" aria-hidden="true"></span>
      <p class="company-name">BRIGHT VALE WORKS</p>
    </div>
    <p class="address-band">3807 Morrow Lane, Suite 412 East Brookridge, NJ 07315</p>
  </section>
</main>
</body>
</html>
```